I have a tallow based business and I want to streamline my products

I have roughly 10 items that I would like to make lebals for in order to streamline my business, I am attaching the current design and am willing to work with this but would also like to see if you come up with something different, my biggest seller is my facewash , my webpage is theplumwrenco,com my current designs are below- The newest one is the light brown version which I do like but I am not sure how that will integrate or be streamlined with the remaining products, If you believe it can look similar and still be attractive, I am ok with that too,

My current Label Project Needs:

Tallow + Magnesium Lotion biodegradable wheat bottle
Tallow Cream Face Wash - biodegradable what bottle
Tallow Body Butter 8 oz jar with bamboo lid
Tallow Deodorant will be printed on a Kraft Paper tube
Tallow Face Cream for Day wear 2 oz glass jar with bamboo lid
Vitamin C Serum 2 oz serum bottle with bamboo pump
Blue Algae Toner 4 oz glass bottle
Tallow + Hyaluronic 2oz face cream jar
'
My project is to display sustainable products, eco friendly packaging, organic , natural and holistic

I am ok with the newest label I attached but I am also ok with a minimalistic project, I would love to choose from a couple of designs.

Thank you so much

```html
<!DOCTYPE html>
<html lang="en">
<head>
<meta charset="utf-8">
<title>Tallow + Magnesium Body Lotion Label</title>
<link href="https://fonts.googleapis.com/css2?family=Jost:wght@300;400;500;600;700&display=swap" rel="stylesheet">
<style>
  :root {
    --ink: #3d4356;
    --paper: #ffffff;
    --silver-dark: #b4b5b8;
    --silver-mid: #cfd0d2;
    --silver-light: #eef0f2;
    --white: #ffffff;
  }
  * { box-sizing: border-box; margin: 0; padding: 0; }
  html, body {
    width: 1200px; height: 734px; overflow: hidden;
    background: var(--paper);
    font-family: "Jost", sans-serif;
    color: var(--ink);
  }
  .canvas { position: relative; width: 1200px; height: 734px; }
  .label {
    position: absolute; left: 108px; top: 108px; width: 984px; height: 518px;
    background: linear-gradient(90deg,
      var(--silver-dark) 0%, var(--silver-mid) 6%, var(--silver-light) 12%,
      var(--silver-mid) 20%, var(--silver-dark) 27%, var(--silver-mid) 36%,
      var(--silver-light) 44%, var(--white) 52%, var(--silver-light) 60%,
      var(--silver-mid) 70%, var(--silver-light) 78%, var(--silver-mid) 86%,
      var(--silver-dark) 94%, var(--silver-mid) 100%);
    overflow: hidden;
  }
  .brand-tab {
    position: absolute; left: 377px; top: 0; width: 232px; height: 58px;
    background: var(--ink); color: var(--white);
    display: flex; align-items: center; justify-content: center;
    font-size: 20px; font-weight: 400; letter-spacing: 1.2px; white-space: nowrap;
  }
  .feature { position: absolute; width: 120px; text-align: center; }
  .feature-icon {
    display: block; margin: 0 auto 8px; width: 70px; height: 44px;
    border-radius: 6px; background: rgba(61,67,86,0.22);
  }
  .feature-name {
    font-size: 13px; font-weight: 500; line-height: 14px; letter-spacing: 0.6px; white-space: nowrap;
  }
  .f1 { left: 20px; top: 100px; }
  .f2 { left: 143px; top: 100px; }
  .f3 { left: 20px; top: 204px; }
  .f4 { left: 148px; top: 204px; }
  .element-tile {
    position: absolute; left: 353px; top: 106px; width: 80px; height: 80px;
    border: 4px solid var(--ink); border-radius: 6px; background: rgba(255,255,255,0.15);
  }
  .element-tile .num { position: absolute; left: 4px; top: 3px; font-size: 7px; }
  .element-tile .mass { position: absolute; right: 5px; top: 3px; font-size: 7px; }
  .element-tile .symbol {
    position: absolute; left: 0; right: 0; top: 16px; text-align: center;
    font-size: 28px; font-weight: 700; line-height: 32px;
  }
  .element-tile .name {
    position: absolute; left: 0; right: 0; bottom: 6px; text-align: center; font-size: 7px;
  }
  .hero-art {
    position: absolute; left: 408px; top: 104px; width: 234px; height: 190px;
    border-radius: 40% 45% 20% 20%;
    background: radial-gradient(ellipse at 55% 45%, rgba(61,67,86,0.55), rgba(61,67,86,0.25) 55%, rgba(61,67,86,0) 75%);
  }
  .product-line {
    position: absolute; left: 292px; top: 308px; width: 410px; text-align: center;
    font-size: 29px; font-weight: 500; letter-spacing: 0.4px; line-height: 34px;
    white-space: nowrap;
  }
  .product-name {
    position: absolute; left: 322px; top: 350px; width: 349px; height: 56px;
    border: 3px solid var(--ink);
    display: flex; align-items: center; justify-content: center;
    font-size: 44px; font-weight: 600; letter-spacing: 2px; line-height: 1; white-space: nowrap;
  }
  .tagline {
    position: absolute; left: 290px; top: 416px; width: 413px; text-align: center;
    font-size: 13.5px; font-weight: 600; line-height: 17px; letter-spacing: 0.5px; white-space: nowrap;
  }
  .net-weight {
    position: absolute; left: 300px; top: 488px; width: 393px; text-align: center;
    font-size: 17px; font-weight: 600; letter-spacing: 0.8px; white-space: nowrap;
  }
  .maker { position: absolute; left: 18px; top: 418px; white-space: nowrap; }
  .maker-intro { font-size: 14px; font-weight: 300; letter-spacing: 0.4px; line-height: 20px; }
  .maker-name { font-size: 17px; font-weight: 600; letter-spacing: 0.8px; line-height: 25px; }
  .maker-address { font-size: 15px; font-weight: 300; letter-spacing: 0.6px; line-height: 22px; }
  .maker-web { font-size: 14px; font-weight: 300; letter-spacing: 0.4px; line-height: 21px; }
  .ingredients {
    position: absolute; left: 637px; top: 171px; width: 466px; height: 185px;
    transform: rotate(-90deg); transform-origin: center;
    font-size: 16.6px; line-height: 20.6px; letter-spacing: 0.5px;
    white-space: nowrap; font-weight: 400;
  }
  .ingredients-title { font-weight: 700; letter-spacing: 0.8px; }
</style>
</head>
<body>
<div class="canvas">
  <section class="label">
    <div class="brand-tab">THE PLUM WREN CO.</div>

    <div class="feature f1"><span class="feature-icon" role="img" aria-label="Icon of a grazing cow"></span><p class="feature-name">GRASS FED<br>TALLOW</p></div>
    <div class="feature f2"><span class="feature-icon" role="img" aria-label="Icon of a cream jar with a sprout"></span><p class="feature-name">ORGANIC<br>INGREDIENTS</p></div>
    <div class="feature f3"><span class="feature-icon" role="img" aria-label="Icon of hands holding a heart"></span><p class="feature-name">HAND<br>CRAFTED</p></div>
    <div class="feature f4"><span class="feature-icon" role="img" aria-label="Icon of a market stall with a handshake"></span><p class="feature-name">FAIR<br>TRADE</p></div>

    <div class="element-tile">
      <span class="num">12</span><span class="mass">24.305</span>
      <span class="symbol">Mg</span><span class="name">Magnesium</span>
    </div>

    <div class="hero-art" role="img" aria-label="Engraved illustration of a grazing dairy cow"></div>

    <h2 class="product-line">TALLOW + MAGNESIUM</h2>
    <h1 class="product-name">BODY LOTION</h1>
    <p class="tagline">MAGNESIUM INFUSED LOTION THAT<br>PROMOTES SKIN NOURISHMENT AND HEALING</p>
    <p class="net-weight">NET WT. 8OZ (236ML))</p>

    <div class="maker">
      <p class="maker-intro">MANUFACTURED BY</p>
      <p class="maker-name">FERNHOLLOW PURE ORGANICS</p>
      <p class="maker-address">PO. BOX 4180 ELMSTEAD, VA 20417</p>
      <p class="maker-web">THEPLUMWRENCO.COM</p>
    </div>

    <div class="ingredients">
      <p class="ingredients-title">OUR AMAZING INGREDIENTS:</p>
      <p>Distilled Water, Lavender Hydrosol, Glycerin, Grass Fed<br>
      Tallow, Daucus Carota (Carrot Seed Oil), Oenothera<br>
      Biennis (Rosehip Oil), Simmondsia Chinensis(Jojoba Oil)<br>
      Cocos Nucifera (Coconut Oil), Cucurbita Pepo Seed Oil<br>
      (Pumpkin Seed Oil)Coenzyme Q10 ( CoQ10<br>
      )Niacinamide, Vitamin B3 Citrus Paradisi Seed Oil<br>
      (Grapefruit Seed oil), Decyl Glucoside, Cetyl Alcohol Citric<br>
      Acid, Xanthan Gum, Sodium Benzoate (Preservative)</p>
    </div>
  </section>
</div>
</body>
</html>
```